5868 7090

Web(re)design of an existing directory search site www.le7090x.be (in Dutch www.de5868x.be and in English www.3969x.be).

This site is a directory site, i.e. a "white pages" site whereby people can search the phone & details of another person based on a combination of name + city (for instance darrow in Brussels); one can also search a company also based on a combination of name + city (for instance Vornex in Brussels); last but not least one can also search the name of the subscriber behind a specific telephone number (also called reverse search).

This site is quite outdated and needs a redesign, see instructions.

We need the output in XD format.

```html
<!DOCTYPE html>
<html lang="fr">
<head>
<meta charset="utf-8">
<title>5868 7090 — Les Renseignements Utiles</title>
<link href="https://fonts.googleapis.com/css2?family=Roboto+Condensed:wght@300;400;700&family=Roboto:wght@400&display=swap" rel="stylesheet">
<style>
  :root{
    --red:#d7141a;
    --red-dark:#c00d12;
    --ink:#1c1c1c;
    --muted:#555;
    --panel:#efefef;
    --line:#c9c9c9;
    --white:#fff;
    --photo-a:#c9a27a;
    --photo-b:#8a6a55;
  }
  *{box-sizing:border-box;margin:0;padding:0}
  html,body{width:1200px;height:600px;overflow:hidden;background:var(--white)}
  body{position:relative;font-family:"Roboto Condensed",sans-serif;color:var(--ink)}

  .site-header{position:absolute;left:0;top:0;width:1200px;height:120px;background:var(--white)}
  .brand{position:absolute;left:171px;top:38px;display:flex;align-items:center;gap:8px;font-weight:700;font-size:28px;color:var(--red)}
  .brand-dot{width:22px;height:22px;border-radius:50%;background:var(--red)}
  .site-title{position:absolute;left:0;width:1200px;top:38px;text-align:center;font-weight:700;font-size:27px;letter-spacing:-.2px}
  .site-title .accent{color:var(--red)}
  .lang{position:absolute;left:953px;top:46px;font-size:17px;color:#444;display:flex;align-items:center;gap:5px}
  .menu-toggle{position:absolute;left:1015px;top:50px}

  .search-panel{position:absolute;left:0;top:120px;width:682px;height:400px;background:var(--panel)}
  .tabs{position:absolute;left:172px;top:51px;display:flex;gap:5px}
  .tab{height:31px;background:var(--white);font-size:16.5px;display:flex;align-items:center;justify-content:center;color:#333}
  .tab.active{background:var(--red);color:var(--white)}
  .field{position:absolute;width:225px;height:31px;background:var(--white);border:1px solid var(--line);font-weight:700;font-size:13.5px;padding-left:13px;display:flex;align-items:center}
  .hint{position:absolute;font-size:11.5px;color:#444;font-weight:300}
  .search-btn{position:absolute;left:415px;top:205px;width:225px;height:31px;background:linear-gradient(var(--red),var(--red-dark));color:var(--white);font-weight:700;font-size:14.5px;display:flex;align-items:center;justify-content:center;gap:10px}
  .captcha{position:absolute;left:170px;top:292px;width:224px;height:54px;background:#f9f9f9;border:1px solid #d3d3d3;font-family:"Roboto",sans-serif;font-size:10.5px}
  .captcha .box{position:absolute;left:8px;top:15px;width:20px;height:20px;border:2px solid #c1c1c1;border-radius:2px;background:var(--white)}
  .captcha .label{position:absolute;left:38px;top:20px}
  .captcha .mark{position:absolute;right:13px;top:10px;width:20px;height:20px;background:#9aa6b8;border-radius:3px}
  .captcha .small{position:absolute;right:7px;top:34px;font-size:6.5px;color:#555;text-align:center;line-height:1.3}

  .hero-photo{position:absolute;left:682px;top:120px;width:518px;height:400px;background:radial-gradient(circle at 60% 45%,var(--photo-a),var(--photo-b) 75%)}

  .site-footer{position:absolute;left:0;top:520px;width:1200px;height:80px}
  .footer-links{position:absolute;left:171px;top:24px;font-size:13.5px;color:#333;display:flex;gap:10px}
  .footer-links .sep{color:#bbb}
  .copyright{position:absolute;left:171px;top:45px;font-size:13.5px;color:#333}
  .partner{position:absolute;left:936px;top:30px;display:flex;align-items:center;gap:5px;font-size:10px;color:var(--ink)}
  .partner-dot{width:11px;height:11px;border-radius:50%;background:var(--red)}
</style>
</head>
<body>
  <header class="site-header">
    <div class="brand"><span class="brand-dot"></span>5868 7090</div>
    <h1 class="site-title">Les Renseignements <span class="accent">SEPTANTE-NONANTE</span> Utiles</h1>
    <div class="lang">FR
      <svg width="9" height="6" viewBox="0 0 9 6"><path d="M1 1l3.5 3.5L8 1" fill="none" stroke="#666" stroke-width="1.2"/></svg>
    </div>
    <svg class="menu-toggle" width="23" height="15" viewBox="0 0 23 15" aria-label="Menu">
      <rect y="0" width="23" height="2" fill="#333"/><rect y="6.5" width="23" height="2" fill="#333"/><rect y="13" width="23" height="2" fill="#333"/>
    </svg>
  </header>

  <main class="search-panel">
    <nav class="tabs">
      <div class="tab active" style="width:101px">Particuliers</div>
      <div class="tab" style="width:100px">Sociétés</div>
      <div class="tab" style="width:138px">Annuaire inversé</div>
      <div class="tab" style="width:107px">International</div>
    </nav>

    <div class="field" style="left:170px;top:121px">Nom de famille:</div>
    <div class="hint" style="left:177px;top:162px">Ex: Dupont, Janssens, ...</div>
    <div class="field" style="left:415px;top:121px">Localité:</div>
    <div class="hint" style="left:422px;top:162px">Ex: Liége, Anvers, 1150, ....</div>
    <div class="field" style="left:170px;top:205px">Prénom:</div>
    <div class="hint" style="left:177px;top:246px">Ex: Jan, Louis, ...</div>

    <div class="search-btn">
      <svg width="18" height="18" viewBox="0 0 18 18"><circle cx="7.5" cy="7.5" r="6" fill="none" stroke="#fff" stroke-width="1.3"/><path d="M12 12l5 5" stroke="#fff" stroke-width="1.3"/></svg>
      70-90!
    </div>

    <div class="captcha">
      <span class="box"></span>
      <span class="label">I'm not a robot</span>
      <span class="mark"></span>
      <span class="small">HumanCheck<br>Privacy - Terms</span>
    </div>
  </main>

  <div class="hero-photo" role="img" aria-label="Photo d'une femme souriante consultant son téléphone en terrasse"></div>

  <footer class="site-footer">
    <div class="footer-links">
      <span>B2B Services</span><span class="sep">|</span>
      <span>Aide</span><span class="sep">|</span>
      <span>Conditions générales d'utilisation</span><span class="sep">|</span>
      <span>Respect de la vie privée</span>
    </div>
    <div class="copyright">Copyright Orvane 2022, tous droits réservés.</div>
    <div class="partner"><span class="partner-dot"></span>www.de5868x.be</div>
  </footer>
</body>
</html>
```